Web Design Project - Event Management Company

A web-page design needs to be created for an event management company. The logo has already been created, the design needs to draw on the themes and colors of the logo and extend on that.

The event management company likes to differentiate itself from others by being a bit "un-conventional" and being able to think outside the box.

the specialise in corporate events, weddings, AGMs, anything that requires coordination of resources. They also can provide Audio Visual services such as recording events.

final design will also require HTML implementation

```html
<!DOCTYPE html>
<html lang="en">
<head>
<meta charset="utf-8">
<title>Offset Block Group — Event Management</title>
<link rel="stylesheet" href="https://fonts.googleapis.com/css2?family=Open+Sans:wght@300;400&family=Raleway:wght@300;400&display=swap">
<style>
  :root {
    --cyan: #00aedb;
    --orange: #eb5e28;
    --lime: #cdd427;
    --ink: #1e1e1e;
    --body: #555555;
    --muted: #9a9a9a;
    --faint: #b5b5b5;
    --rule: #e2e2e2;
    --social: #c9c9c9;
    --paper: #ffffff;
  }
  * { box-sizing: border-box; margin: 0; padding: 0; }
  html, body { width: 1200px; height: 1200px; overflow: hidden; background: var(--paper); }
  body { position: relative; font-family: "Open Sans", Arial, sans-serif; color: var(--body); }
  .abs { position: absolute; }

  /* Header */
  .brand { left: 87px; top: 62px; display: flex; align-items: center; gap: 10px; }
  .brand-mark { width: 20px; height: 20px; background: var(--cyan); }
  .brand-name { font-family: "Open Sans", Arial, sans-serif; font-weight: 400; font-size: 24px; color: #333; letter-spacing: 0.5px; text-transform: uppercase; }
  .social { top: 32px; left: 1019px; display: flex; gap: 7px; }
  .social span { width: 28px; height: 28px; border-radius: 50%; background: var(--social); display: block; }

  .main-nav { left: 653px; top: 89px; display: flex; gap: 3px; }
  .main-nav a { display: block; height: 41px; line-height: 41px; background: var(--cyan); color: #fff; text-decoration: none; font-family: "Raleway", Arial, sans-serif; font-size: 13.5px; letter-spacing: 0.3px; text-align: center; }
  .nav-home { width: 82px; } .nav-services { width: 129px; } .nav-portfolio { width: 112px; } .nav-contact { width: 133px; }
  .nav-rule { left: 82px; top: 132px; width: 1037px; height: 3px; background: var(--cyan); }

  /* Hero */
  .hero { left: 84px; top: 136px; width: 1035px; height: 394px;
    background: linear-gradient(180deg, #c9c27a 0%, #b7b96a 30%, #6d6c3f 62%, #3a3527 100%); }
  .hero::before { content: ""; position: absolute; inset: 0;
    background: linear-gradient(90deg, rgba(214,96,120,.35) 0%, rgba(190,210,80,.25) 40%, rgba(220,100,120,.25) 70%, rgba(150,200,60,.2) 100%); }
  .video-player { left: 100px; top: 264px; width: 418px; height: 249px; background: rgba(28,28,28,.82); }

  /* Service tiles */
  .tile { top: 563px; width: 338px; height: 160px; color: #fff; padding: 22px 0 0 26px; }
  .tile-corporate { left: 85px; background: var(--cyan); }
  .tile-weddings { left: 434px; background: var(--orange); }
  .tile-av { left: 782px; background: var(--lime); }
  .tile-head { display: flex; align-items: center; gap: 10px; height: 32px; }
  .tile-title { font-family: "Raleway", Arial, sans-serif; font-size: 21px; letter-spacing: 0.4px; text-transform: uppercase; }
  .tile-text { margin-top: 8px; font-size: 12px; line-height: 17px; width: 300px; }

  /* Content */
  .section-title { font-family: "Raleway", Arial, sans-serif; font-size: 21px; color: var(--ink); text-transform: uppercase; letter-spacing: 0.2px; }
  .welcome-title { left: 87px; top: 766px; }
  .latest-title { left: 826px; top: 766px; }
  .welcome-text { left: 86px; top: 813px; width: 695px; font-size: 12px; line-height: 17px; }
  .event-image { left: 828px; top: 817px; width: 295px; height: 82px;
    background: linear-gradient(160deg, #9fc6e6 0%, #3d76b0 45%, #18365e 100%); }
  .event-text { left: 828px; top: 917px; width: 300px; font-size: 12px; line-height: 17px; }

  /* Footer */
  .footer-rule { left: 82px; top: 1001px; width: 1037px; height: 1px; background: var(--rule); }
  .footer-col { top: 1024px; }
  .footer-col h4 { font-family: "Raleway", Arial, sans-serif; font-weight: 400; font-size: 15px; color: var(--muted); margin-bottom: 10px; }
  .footer-col li { list-style: none; font-size: 11px; line-height: 22px; color: var(--faint); }
  .col-cases { left: 92px; } .col-about { left: 245px; } .col-portfolio { left: 446px; }
  .col-news { left: 592px; } .col-contacts { left: 804px; }
  .footer-mark { left: 1040px; top: 1060px; width: 34px; height: 34px; background: var(--orange); }
  .base-rule { left: 82px; top: 1167px; width: 1037px; height: 1px; background: var(--rule); }
  .base-links { left: 83px; top: 1176px; display: flex; gap: 17px; font-size: 9px; color: var(--faint); }
  .copyright { right: 80px; top: 1176px; font-size: 9px; color: var(--faint); }
</style>
</head>
<body>

<header>
  <div class="abs brand"><span class="brand-mark"></span><span class="brand-name">Offset Block Group</span></div>
  <div class="abs social" aria-label="Social links"><span></span><span></span><span></span></div>
  <nav class="abs main-nav">
    <a class="nav-home" href="#">HOME</a>
    <a class="nav-services" href="#">OUR SERVICES</a>
    <a class="nav-portfolio" href="#">PORTFOLIO</a>
    <a class="nav-contact" href="#">CONTACT US</a>
  </nav>
  <div class="abs nav-rule"></div>
</header>

<section class="abs hero" role="img" aria-label="Photo of a banquet hall set for an event, with pink and green lit drapes, a projection screen and floral table centrepieces"></section>

<div class="abs video-player">
  <svg width="418" height="249" viewBox="0 0 418 249">
    <circle cx="184" cy="114" r="30" fill="rgba(255,255,255,.08)" stroke="#bdbdbd" stroke-width="3"/>
    <path d="M175 98 L200 114 L175 130 Z" fill="#bdbdbd"/>
    <path d="M23 199 L31 205 L23 211 Z" fill="#fff"/>
    <text x="44" y="208" font-family="Open Sans, sans-serif" font-size="7" fill="#ddd">00:00</text>
    <rect x="68" y="204" width="230" height="3" fill="#3a3a3a"/>
    <path d="M304 203 h3 l3 -3 v10 l-3 -3 h-3 z" fill="#fff"/>
    <g fill="#fff">
      <rect x="313" y="201" width="1.5" height="8"/><rect x="316" y="201" width="1.5" height="8"/>
      <rect x="319" y="201" width="1.5" height="8"/><rect x="322" y="201" width="1.5" height="8"/>
      <rect x="325" y="201" width="1.5" height="8"/><rect x="328" y="201" width="1.5" height="8"/>
      <rect x="331" y="201" width="1.5" height="8"/><rect x="334" y="201" width="1.5" height="8"/>
    </g>
  </svg>
</div>

<section class="abs tile tile-corporate">
  <div class="tile-head">
    <svg width="30" height="28" viewBox="0 0 30 28" fill="none" stroke="#fff" stroke-width="1.8">
      <circle cx="5" cy="22" r="3"/><circle cx="13" cy="24" r="3"/><circle cx="24" cy="14" r="3"/>
      <path d="M4 6 l4 4 M8 6 l-4 4"/><path d="M10 8 q8 -6 14 3" stroke-dasharray="2 2"/>
    </svg>
    <h2 class="tile-title">Corporate Events</h2>
  </div>
  <p class="tile-text">Lorem ipsum dolor sit amet consectetur adipiscing elit. Sed rhoncus faucibus faucibus. Maecenas erat odio, mattis is suscipit a ullamcorper nec felis. Pellentesque ut sem et ante condimentum</p>
</section>

<section class="abs tile tile-weddings">
  <div class="tile-head">
    <svg width="28" height="32" viewBox="0 0 28 32" fill="none" stroke="#fff" stroke-width="3">
      <circle cx="14" cy="20" r="9"/><path d="M10 5 l4 -3 l4 3 l-4 4 z" fill="#fff" stroke-width="1"/>
    </svg>
    <h2 class="tile-title">Weddings</h2>
  </div>
  <p class="tile-text">Lorem ipsum dolor sit amet consectetur adipiscing elit. Sed rhoncus faucibus faucibus. Maecenas erat odio, mattis is suscipit a ullamcorper nec felis. Pellentesque ut sem et ante condimentum</p>
</section>

<section class="abs tile tile-av">
  <div class="tile-head">
    <svg width="30" height="32" viewBox="0 0 30 32" fill="#fff">
      <circle cx="7" cy="6" r="5"/><circle cx="17" cy="6" r="5"/>
      <rect x="3" y="12" width="18" height="10"/><path d="M21 15 l7 -4 v12 l-7 -4 z"/>
      <path d="M11 22 l-5 9 M11 22 l5 9" stroke="#fff" stroke-width="2"/>
    </svg>
    <h2 class="tile-title">Audio Visuals</h2>
  </div>
  <p class="tile-text">Lorem ipsum dolor sit amet consectetur adipiscing elit. Sed rhoncus faucibus faucibus. Maecenas erat odio, mattis is suscipit a ullamcorper nec felis. Pellentesque ut sem et ante condimentum</p>
</section>

<main>
  <h1 class="abs section-title welcome-title">Welcome to Offset Block Group</h1>
  <div class="abs welcome-text">
    <p>Lorem ipsum dolor sit amet, consectetur adipiscing elit. Sed rhoncus faucibus faucibus. Maecenas erat odio, mattis id suscipit a, ullamcorper nec felis. Pellentesque ut sem et ante condimentum ultrices quis nec lorem. Integer non sem justo. Praesent malesuada, nulla id elementum aliquam, elit erat tincidunt justo, ut posuere erat metus eu turpis. Pellentesque habitant morbi tristique senectus et netus et malesuada fames ac turpis egestas. Donec tempus congue sem, sed volutpat justo mollis semper. Phasellus facilisis, dui sed elementum pretium, metus sapien scelerisque orci, ut accumsan nisi dui at felis. Integer pulvinar justo eu arcu rutrum ornare.</p>
    <p>Donec tempus congue sem, sed volutpat justo mollis semper. Phasellus facilisis, dui sed elementum pretium, metus sapien scelerisque orci, ut accumsan nisi dui at felis. Integer pulvinar justo eu arcu rutrum ornare.</p>
  </div>

  <h2 class="abs section-title latest-title">Latest Event</h2>
  <div class="abs event-image" role="img" aria-label="Photo looking up at glass office towers against a blue sky"></div>
  <p class="abs event-text">Lorem ipsum dolor sit amet, consectetur adipiscing elit. Sed rhoncus faucibus faucibus. Maecenas erat</p>
</main>

<footer>
  <div class="abs footer-rule"></div>
  <div class="abs footer-col col-cases"><h4>Case studies</h4><ul><li>Tradeshows</li><li>Events</li><li>Festivals</li><li>Tours</li></ul></div>
  <div class="abs footer-col col-about"><h4>About us</h4><ul><li>Staff</li><li>Company history</li><li>The management</li><li>Employment opportunities</li></ul></div>
  <div class="abs footer-col col-portfolio"><h4>Portfolio</h4><ul><li>Slideshow</li><li>Our clients</li><li>Photo gallery</li><li>Our services</li></ul></div>
  <div class="abs footer-col col-news"><h4>News &amp; testimonials</h4><ul><li>Reviews</li><li>News</li><li>Photo gallery</li><li>Client testimonials</li></ul></div>
  <div class="abs footer-col col-contacts"><h4>Contacts</h4><ul><li>080 41170, 080 52296</li><li>hello@offsetblock.com</li><li>48 Harlow Street</li><li>Fairview</li></ul></div>
  <div class="abs footer-mark"></div>
  <div class="abs base-rule"></div>
  <div class="abs base-links"><span>Home</span><span>About Us</span><span>Contact Us</span><span>Privacy Policy</span><span>Sitemap</span></div>
  <div class="abs copyright">Offsetblock. Copyright 2013. All rights reserved</div>
</footer>

</body>
</html>
```